Card design for orthopaedic surgeons working as The Brindlewood Orthopaedic Centre

Business cards, letterhead

Colors

Designer to choose colors to be used in the design.

Requirements
Must have
• Late addition.
• Cards letterhead must have logos of
• Corvane Federated Institute of Surgeons
• Meridale Orthopaedic Society
Nice to have
• Back of card to have space for appointment time to be added by hand and some blank space for writing incidental other notes.

```html
<!DOCTYPE html>
<html lang="en">
<head>
<meta charset="utf-8">
<title>The Brindlewood Orthopaedic Centre – Stationery</title>
<link rel="stylesheet" href="https://fonts.googleapis.com/css2?family=Questrial&family=Open+Sans:wght@400;700&display=swap">
<style>
  :root {
    --stage: #d9dadb;
    --paper: #ffffff;
    --sky: #36b2f8;
    --brand: #2a9fe0;
    --navy: #17324a;
    --ink: #ffffff;
    --badge: #e4edf3;
    --badge-on-sky: rgba(255, 255, 255, 0.55);
  }
  * { margin: 0; padding: 0; box-sizing: border-box; }
  html, body { width: 1200px; height: 800px; overflow: hidden; }
  body {
    background: var(--stage);
    font-family: "Open Sans", Arial, sans-serif;
    position: relative;
  }
  .sheet {
    position: absolute;
    background: var(--paper);
    overflow: hidden;
  }
  .sheet svg.waves { position: absolute; inset: 0; width: 100%; height: 100%; }
  .wave-fill { fill: var(--sky); }
  .wave-line { fill: none; stroke: var(--paper); stroke-width: 3; }
  .wave-accent { fill: none; stroke: var(--navy); stroke-width: 3; stroke-linecap: round; }

  .wordmark {
    position: absolute;
    font-family: "Questrial", Arial, sans-serif;
    color: var(--brand);
    white-space: nowrap;
    letter-spacing: -0.2px;
  }
  .info {
    position: absolute;
    color: var(--ink);
    font-size: 7px;
    line-height: 11px;
    white-space: nowrap;
  }
  .info .dot {
    display: inline-block; width: 5px; height: 5px; border-radius: 50%;
    background: var(--ink); margin-right: 2px; vertical-align: 0;
  }

  /* partner association badges */
  .partners { position: absolute; display: flex; gap: 6px; }
  .partner-badge { display: block; border-radius: 50%; background: var(--badge-on-sky); }
  .card-front .partners { right: 14px; top: 134px; }
  .card-back .partners { right: 14px; top: 122px; }
  .card-front .partner-badge,
  .card-back .partner-badge { width: 16px; height: 16px; }
  .letterhead .partners { left: 30px; top: 40px; gap: 10px; }
  .letterhead .partner-badge { width: 44px; height: 44px; background: var(--badge); }

  /* business card front */
  .card-front { left: 146px; top: 282px; width: 276px; height: 156px; }
  .card-front .wordmark { left: 0; right: 0; top: 55px; text-align: center; font-size: 13.5px; }
  .card-front .info { left: 44px; top: 136px; }

  /* business card back */
  .card-back { left: 146px; top: 480px; width: 276px; height: 157px; }
  .card-back .wordmark { left: 15px; top: 28px; font-size: 10px; }
  .card-back .holder { position: absolute; right: 15px; top: 18px; text-align: right; }
  .card-back .holder-name { color: var(--sky); font-weight: 700; font-size: 14px; line-height: 18px; }
  .card-back .holder-role { color: var(--navy); font-size: 7.5px; line-height: 10px; }
  .card-back .info { left: 40px; top: 121px; }

  /* letterhead */
  .letterhead { left: 531px; top: 61px; width: 524px; height: 678px; }
  .letterhead .wordmark { right: 26px; top: 56px; font-size: 14.5px; }
  .letterhead .web { position: absolute; left: 354px; top: 606px; color: var(--navy); font-size: 8.5px; }
  .letterhead .web .dot { display: inline-block; width: 7px; height: 7px; border-radius: 50%; background: var(--sky); margin-right: 4px; }
  .letterhead .info { left: 45px; top: 630px; font-size: 8.5px; line-height: 13px; }
</style>
</head>
<body>

  <section class="sheet card-front" aria-label="Business card front">
    <svg class="waves" viewBox="0 0 276 156" preserveAspectRatio="none" aria-hidden="true">
      <path class="wave-fill" d="M0,126 C50,96 110,88 160,100 C205,112 240,126 276,120 L276,156 L0,156 Z"/>
      <path class="wave-line" d="M0,134 C50,104 110,96 160,108 C205,120 240,134 276,128"/>
      <path class="wave-accent" d="M150,96 C195,108 235,118 276,106"/>
    </svg>
    <div class="wordmark">The Brindlewood Orthopaedic Centre</div>
    <div class="info">Web : xxxxxxxxxxxxxxxxx</div>
    <div class="partners">
      <span class="partner-badge" role="img" aria-label="Corvane Federated Institute of Surgeons badge"></span>
      <span class="partner-badge" role="img" aria-label="Meridale Orthopaedic Society badge"></span>
    </div>
  </section>

  <section class="sheet card-back" aria-label="Business card back">
    <svg class="waves" viewBox="0 0 276 157" preserveAspectRatio="none" aria-hidden="true">
      <path class="wave-fill" d="M0,92 C50,62 110,54 160,66 C205,78 240,92 276,86 L276,157 L0,157 Z"/>
      <path class="wave-line" d="M0,100 C50,70 110,62 160,74 C205,86 240,100 276,94"/>
      <path class="wave-accent" d="M150,62 C195,74 235,84 276,72"/>
    </svg>
    <div class="wordmark">The Brindlewood Orthopaedic Centre</div>
    <div class="holder">
      <div class="holder-name">NAME</div>
      <div class="holder-role">Designation</div>
    </div>
    <div class="info">
      <div><span class="dot"></span>Address xxxxxxxxxxxxxxxxxxxxxxxxxxxxx</div>
      <div><span class="dot"></span>Mobile xxxxxxxxxxx &nbsp;<span class="dot"></span>Email ID xxxxxxxxxxxx</div>
    </div>
    <div class="partners">
      <span class="partner-badge" role="img" aria-label="Corvane Federated Institute of Surgeons badge"></span>
      <span class="partner-badge" role="img" aria-label="Meridale Orthopaedic Society badge"></span>
    </div>
  </section>

  <section class="sheet letterhead" aria-label="Letterhead">
    <svg class="waves" viewBox="0 0 524 678" preserveAspectRatio="none" aria-hidden="true">
      <path class="wave-fill" d="M0,629 C60,592 140,575 220,584 C320,596 420,640 524,640 L524,678 L0,678 Z"/>
      <path class="wave-line" d="M0,641 C60,604 140,587 220,596 C320,608 420,652 524,652"/>
      <path class="wave-accent" d="M300,604 C370,628 455,634 524,600"/>
    </svg>
    <div class="partners">
      <span class="partner-badge" role="img" aria-label="Corvane Federated Institute of Surgeons badge"></span>
      <span class="partner-badge" role="img" aria-label="Meridale Orthopaedic Society badge"></span>
    </div>
    <div class="wordmark">The Brindlewood Orthopaedic Centre</div>
    <div class="web"><span class="dot"></span>Web : xxxxxxxxxxxxxxxxx</div>
    <div class="info">
      <div><span class="dot"></span>Address xxxxxxxxxxxxxxxxxxxxxxxxxxxxxxxxxxxxxxx</div>
      <div><span class="dot"></span>Mobile xxxxxxxxxxx &nbsp;<span class="dot"></span>Email ID xxxxxxxxxxxxxxxxxxx</div>
    </div>
  </section>

</body>
</html>
```